Health & Fitness Author & Public Speaker Needs Visually Stunning Web Redesign!

It's time for a redesign of the home page for Verity Halloway's "Bright Fork Kitchen" website (www.brightforkkitchen-example.com). We have a VERY clear idea of what we want, so it really won't take a talented designer long to bring it to life.
The website itself is used to promote & sell her range of health & nutrition programs to a female audience, primarily aged 24 - 35 working in professional or semi professional occupations.
For a VERY comprehensive outline of exactly what we are after, please see the following attached files:
(1) 'Website - WireFrame' (layout, content/copy, visual design style we want along with the desired color scheme)
(2) 'Website - Style Guide' (these are the colours, and overall feel we want)
PLEASE REVIEW THIS IN FULL - THEY WILL GIVE YOU A VERY CLEAR IDEA OF WHAT WE WANT.
Most of the files you need are attached, but for more photos that you can use (of Verity, her programs, and food/meals) can be found at these URL's:
VERITY (profile photos):
https://www.filebinbox.example/sh/qm3rt8wpz1xkd7a/RtPlm4vaNe
ECOVERS
- Bright Fork Kitchen Guide (ebook): https://www.filebinbox.example/sh/wxtnvo5d274ku22/hBqYrsnoz3
- 21 Week Total Momentum Course (ecourse): https://www.filebinbox.example/sh/zopqinr6a2mhwyl/c-dg341oTR
- E-Magazine Issues:
https://www.filebinbox.example/sh/4pzmkar2s9vtyw/57LeWcdDxpB
STOCK IMAGES:
https://www.filebinbox.example/sh/k2qowr8atbnzlx/Qe3HT5mmDy
As we will need to revamp our existing Facebook page & other printed material, there may be the potential for further work for the successful designer in the future.
Thanks & Good Luck!
Declan Furrow
Marketing & Business Development Manager
Bright Fork Kitchen

```html
<!DOCTYPE html>
<html lang="en">
<head>
<meta charset="utf-8">
<title>Bright Fork Kitchen – Home</title>
<link href="https://fonts.googleapis.com/css2?family=Questrial&family=Kaushan+Script&display=swap" rel="stylesheet">
<style>
:root{
  --purple:#8b1890;
  --purple-soft:rgba(170,80,190,.86);
  --pink:#d4195c;
  --ink:#2b2b2b;
  --text:#444;
  --muted:#777;
  --white:#fff;
  --dark:#111;
  --field:rgba(255,255,255,.35);
}
*{box-sizing:border-box;margin:0;padding:0}
html,body{width:1200px;height:2451px;overflow:hidden;background:#fff}
body{position:relative;font-family:"Questrial",Arial,sans-serif;color:var(--text)}
.abs{position:absolute}

/* hero */
.hero{left:12px;top:0;width:1176px;height:555px;background:linear-gradient(100deg,#d9d4cb 0%,#c9c2b6 35%,#b8b2a8 55%,#8c7f72 70%,#c7c0b5 100%)}
.hero-rule{left:12px;top:553px;width:1176px;height:9px;background:var(--pink)}
.topbar{left:12px;top:0;width:1176px;height:95px;background:rgba(255,255,255,.78)}
.logo{left:95px;top:32px;font-size:26px;color:var(--pink);letter-spacing:-.5px}
.logo::before{content:"";display:inline-block;width:12px;height:12px;background:var(--purple);border-radius:50%;margin-right:8px;vertical-align:middle}
.nav{top:38px;font-size:13px;letter-spacing:.5px;color:#333}
.nav-active{left:915px;top:89px;width:92px;height:6px;background:var(--pink)}
.signup-circle{left:137px;top:35px;width:462px;height:462px;border-radius:50%;background:var(--purple-soft)}
.signup-lead{left:190px;top:168px;width:330px;text-align:center;color:var(--white);font-size:17px;line-height:1.35}
.field{left:198px;width:296px;height:42px;background:var(--field);color:var(--white);font-size:15px;padding:12px 16px}
.join-btn{left:272px;top:388px;width:148px;height:42px;background:#24141f;color:var(--white);font-size:14px;text-align:center;line-height:42px;letter-spacing:1px}
.ribbon{left:190px;top:455px;width:315px;height:48px}
.ribbon-text{left:190px;top:466px;width:315px;text-align:center;font-family:"Kaushan Script",cursive;color:var(--white);font-size:18px}

/* article */
.article{left:96px;top:610px;width:622px}
.article h1{font-weight:400;font-size:20px;line-height:1.35;color:var(--ink);letter-spacing:.5px}
.article p{font-size:11.2px;line-height:1.65;color:var(--text);margin-top:14px}
.article h2{font-weight:400;font-size:19px;color:var(--ink);margin-top:22px}
.video{width:622px;height:313px;margin-top:22px;position:relative;background:linear-gradient(180deg,#5c6b3c 0%,#7b8a4a 40%,#5e6d37 100%);border-radius:3px}
.video .play{position:absolute;left:300px;top:140px}
.video .track{position:absolute;left:120px;right:120px;bottom:16px;height:4px;background:rgba(255,255,255,.4)}
.video .track span{display:block;width:30%;height:100%;background:var(--purple)}
.ticks{list-style:none;margin-top:8px}
.ticks li{font-size:11.2px;line-height:1.6;padding-left:22px;position:relative;margin-bottom:3px}
.ticks li::before{content:"";position:absolute;left:0;top:3px;width:12px;height:12px;background:var(--pink)}
.share{left:96px;top:2010px;width:622px;height:24px}
.share-btn{left:0;top:0;width:136px;height:24px;background:var(--purple);color:var(--white);font-size:11.5px;text-align:center;line-height:24px;letter-spacing:.5px}
.count{top:1px;height:22px;font-size:11.5px;display:flex;align-items:center}
.count i{display:block;width:22px;height:22px;background:#111;margin-right:6px}
.count b{font-weight:400;background:var(--purple);color:var(--white);padding:0 8px;line-height:22px}

/* sidebar */
.discovered{left:762px;top:612px;font-family:"Kaushan Script",cursive;font-size:19px;color:#222}
.badge{background:#e4e4e4}
.kick{left:762px;top:875px;width:341px;height:288px;background:#d8d8d8;overflow:hidden}
.kick-photo{left:0;top:0;width:341px;height:288px;background:linear-gradient(90deg,#bdbdbd,#e6e6e6 45%,#cfcfcf)}
.kick-circle{left:120px;top:-10px;width:320px;height:320px;border-radius:50%;background:rgba(212,25,92,.82)}
.kick-title{left:150px;top:72px;width:178px;text-align:right;color:var(--white);font-size:19px;line-height:1.2}
.kick-copy{left:150px;top:130px;width:178px;text-align:right;color:var(--white);font-size:16px;line-height:1.35}
.order{left:762px;top:1185px;width:341px;height:288px;background:#e9e9e9}
.order-cover{left:16px;top:12px;width:170px;height:264px;background:linear-gradient(160deg,#e3e3e3,#c9c9c9)}
.order-panel{left:173px;top:0;width:168px;height:288px;background:rgba(164,60,190,.9)}
.order-title{left:190px;top:30px;color:var(--white);font-size:21px}
.order-copy{left:190px;top:70px;width:145px;color:var(--white);font-size:13.5px;line-height:1.45}
.order-limited{left:190px;top:178px;color:var(--white);font-size:13px}
.buy{left:150px;top:222px;width:191px;height:40px;background:var(--pink);color:var(--white);font-size:22px;line-height:40px;padding-left:42px}

/* footer */
.footer{left:12px;top:2118px;width:1176px;height:282px;background:var(--purple)}
.foot-h{left:96px;top:2150px;width:260px;color:var(--white);font-size:14.5px;line-height:1.5}
.foot-s{left:96px;top:2198px;width:220px;color:var(--white);font-size:10.5px;line-height:1.5}
.foot-field{left:96px;width:242px;height:32px;background:var(--white);display:flex;align-items:center;font-size:10px;color:#aaa}
.foot-field i{display:block;width:32px;height:32px;background:#111;margin-right:10px}
.foot-field em{margin-left:auto;margin-right:10px;width:11px;height:11px;border-radius:50%;display:block}
.signin{left:96px;top:2336px;width:134px;height:30px;background:#111;color:var(--white);font-size:11px;text-align:center;line-height:30px}
.need{left:430px;top:2152px;color:var(--white);font-family:"Kaushan Script",cursive;font-size:14px}
.mag{left:435px;top:2190px;width:345px;height:205px;background:linear-gradient(170deg,#f4f2f4,#d9d0da);transform:rotate(-4deg)}
.ult-h{left:803px;top:2220px;color:var(--white);font-size:12.5px;letter-spacing:.3px}
.ult-c{left:803px;top:2248px;width:250px;color:var(--white);font-size:10.5px;line-height:1.5}
.ult-btn{left:803px;top:2305px;width:210px;height:30px;background:#111;color:var(--white);font-size:10.5px;text-align:center;line-height:30px;letter-spacing:.3px}
.bottombar{left:12px;top:2400px;width:1176px;height:51px;background:#0d0d0d}
.legal{left:96px;top:2419px;color:var(--white);font-size:10.5px;word-spacing:3px}
.connect{left:852px;top:2419px;color:var(--white);font-size:10.5px}
.soc{top:2418px;width:14px;height:14px;background:#fff}
</style>
</head>
<body>

<div class="abs hero" role="img" aria-label="Photo of the health coach sitting on a sunny stone ledge, smiling"></div>
<div class="abs topbar"></div>
<div class="abs logo">Bright Fork Kitchen</div>
<div class="abs nav" style="left:680px">ABOUT</div>
<div class="abs nav" style="left:787px">THE FREE PLAN</div>
<div class="abs nav" style="left:942px">BLOG</div>
<div class="abs nav" style="left:1040px">SHOP</div>
<div class="abs nav-active"></div>
<div class="abs hero-rule"></div>

<div class="abs signup-circle"></div>
<p class="abs signup-lead">A weekly serving of motivation, recipes &amp; FREE resources straight to your inbox!</p>
<div class="abs field" style="top:270px">First name</div>
<div class="abs field" style="top:322px">E-mail</div>
<div class="abs join-btn">JOIN</div>
<svg class="abs ribbon" viewBox="0 0 315 48" aria-hidden="true"><path d="M0 4H315L300 24L315 44H0L15 24Z" fill="#d4195c"/></svg>
<div class="abs ribbon-text">Join Bright Fork Kitchen Program</div>

<main class="abs article">
  <h1>WANT A BODY YOU'RE PROUD OF AND A HEALTHY LIFESTYLE YOU LOVE? THEN YOU DON'T NEED ANOTHER DIET!</h1>
  <p>Hey there I'm Verity, I help smart, savvy, driven women just like you to slim down so you can not only rock your outfit but you can enjoy a lifestyle to match. As hard as it might be for you to believe right now, I'll teach you how to have this in a way that's easier, and heaps more enjoyable than you'd ever thought possible – it's time to kiss guilt and deprivation goodbye!</p>
  <div class="video" role="img" aria-label="Video still of the coach sitting on grass in a park">
    <svg class="play" width="26" height="30" viewBox="0 0 26 30"><path d="M0 0L26 15L0 30Z" fill="#fff"/></svg>
    <div class="track"><span></span></div>
  </div>
  <h2>Hmmm... do any of these sound familiar?</h2>
  <ul class="ticks">
    <li>Tried a bunch of diet plans but you're still stuck in body that just feels yuk</li>
    <li>You "know what to do" but somehow you're still not doing it (WTF!)</li>
    <li>Suffer from emotional eating, feelings of guilt or frustration around food &amp; exercise</li>
    <li>Feel bloated, guilty and maybe even a bit ashamed</li>
    <li>Overwhelmed and frustrated at yourself, feel that being slim and fit is a never ending chore</li>
  </ul>
  <p>You're not the only one... heck that was me at one time. But if you're exhausted at not liking your body, and sick of seeing other women make it all look so easy, don't you think maybe it's time to try something new? Perhaps it's time you stopped following what everyone else is doing (girlfriends, the 19 year old receptionist at work, or that really buffed chick at the gym)... obviously it's not working. So what's the alternative?</p>
  <h2>What If I Told You There Was An Easier &amp; More Enjoyable Way?</h2>
  <ul class="ticks">
    <li>To lose weight (most ladies I work with want to lose between 5kg-10kg... sometimes more)</li>
    <li>Have more energy</li>
    <li>Stop feeling bloated and exhausted</li>
    <li>Stop feeling frustrated for eating the "wrong" things and not exercising "enough"</li>
    <li>Feel hot in your clothes, at work and when you go out</li>
    <li>Feel proud of yourself</li>
    <li>Still have a social life... with you know, friends and stuff!</li>
  </ul>
  <p>Ok... sounds good so far right, but you're probably wondering what is about my method that's so different for all the others out there? Honestly, the problem with most other diet programs is that they:</p>
  <ul class="ticks">
    <li>Ignore the importance of pleasure in your life for weight loss. (I think it's key)</li>
    <li>Don't teach you how to never need to be on another program, plan or diet again.</li>
    <li>Focus on what you need to cut out (I focus on what you need more of in your life to make it more pleasurable so you can stop feeding the voids in your life with toxic food, booze, etc)</li>
    <li>Assume you want the same things as everyone else. They assume your definition of healthy should be the same as everyone else's. (I'll teach you what works for you)</li>
    <li>Ignore the impact that stress has on your ability to shift weight (biochemistry can be cruel).</li>
  </ul>
  <p>I get it. I know and understand first hand your frustrations (I used to be you). I know you want it to be effortless. I know you want to not worry about putting on weight EVER, you want to just "Be". You may have some pieces of the puzzle already, but they just never seem to get together for long enough to get the outcome you truly crave – A hot body you're proud of with a healthy lifestyle you love. I get it. I understand. And I can help you get there.</p>
  <p>As a qualified Food &amp; Wellness Coach (and Personal Trainer), I've helped thousands of women (starting with myself) just like you over the last 7+ years to not just lose weight (that's nice) but take back control, regain self confidence and find peace with their bodies (that's better – trust me). You can do it to.</p>
  <p>So what now? First things first, sign up for my E-Magazine below (it's FREE!) to receive some really fantastic recipes, inspirational articles, workouts &amp; expert wellness tips each month.</p>
</main>

<div class="abs share">
  <div class="abs share-btn">SHARE THIS POST</div>
  <div class="abs count" style="left:335px"><i></i><b>15</b></div>
  <div class="abs count" style="left:410px"><i></i><b>34</b></div>
  <div class="abs count" style="left:487px"><i></i><b>162</b></div>
  <div class="abs count" style="left:568px"><i></i><b>7</b></div>
</div>

<aside>
  <div class="abs discovered">Already discovered by...</div>
  <div class="abs" style="left:762px;top:660px;width:110px;height:110px;background:var(--pink)" aria-label="Featured listing badge"></div>
  <div class="abs badge" style="left:890px;top:672px;width:213px;height:32px"></div>
  <div class="abs badge" style="left:892px;top:718px;width:212px;height:50px"></div>
  <div class="abs badge" style="left:762px;top:790px;width:158px;height:52px;background:#f3c6d7"></div>
  <div class="abs badge" style="left:938px;top:800px;width:165px;height:36px"></div>

  <div class="abs kick">
    <div class="abs kick-photo" role="img" aria-label="Black and white portrait of the coach"></div>
    <div class="abs kick-circle"></div>
    <div class="abs kick-title">30 DAY KICK START<br>+ DETOX</div>
    <div class="abs kick-copy">A complete step by step program to get you on the path to a hotter, healthier &amp; happier you!</div>
  </div>

  <div class="abs order">
    <div class="abs order-cover" role="img" aria-label="Ebook cover of the Bright Fork Kitchen Guide"></div>
    <div class="abs order-panel"></div>
    <div class="abs order-title">ORDER TODAY</div>
    <div class="abs order-copy">Yours for the awesome price of just $9.95! (Valued $19.95)</div>
    <div class="abs order-limited">*Limited Time Only</div>
    <div class="abs buy">BUY NOW</div>
  </div>
</aside>

<footer>
  <div class="abs footer"></div>
  <div class="abs foot-h">Get Slim, Boost Energy And Create a Healthy Life You Love!</div>
  <div class="abs foot-s">Subscribe to my FREE monthly e-magazine for heaps of awesome recipes, workouts &amp; advice!</div>
  <div class="abs foot-field" style="top:2250px"><i></i>Username<em style="background:#5cb85c"></em></div>
  <div class="abs foot-field" style="top:2293px"><i></i>Email<em style="background:#d9534f"></em></div>
  <div class="abs signin">Sign in</div>
  <div class="abs need">Need a hand getting started?</div>
  <svg class="abs" style="left:660px;top:2150px" width="30" height="26" viewBox="0 0 30 26" aria-hidden="true"><path d="M2 4C14 2 22 8 24 20M18 16L24 22L28 14" fill="none" stroke="#fff" stroke-width="1.5"/></svg>
  <div class="abs mag" role="img" aria-label="Open e-magazine spread with recipes and photos"></div>
  <div class="abs ult-h">ULTIMATE 30 DAY KICK START PROGRAM</div>
  <div class="abs ult-c">Finally an easy to follow program to help you get slim &amp; eat well, but also help you create a Healthy Life you love!</div>
  <div class="abs ult-btn">I WANT TO JOIN THE PROGRAM</div>
  <div class="abs bottombar"></div>
  <div class="abs legal">Privacy Policy | Returns &amp; Refunds | Contact |</div>
  <div class="abs connect">Connect with Verity</div>
  <div class="abs soc" style="left:982px"></div>
  <div class="abs soc" style="left:1008px"></div>
  <div class="abs soc" style="left:1034px"></div>
  <div class="abs soc" style="left:1060px"></div>
  <div class="abs soc" style="left:1086px"></div>
</footer>

</body>
</html>
```